Clothing range for the petite modern mature woman needs a card design

We need a business card design for a new Sydney based company called lark reed. We provide clothing to the modern mature woman who finds it difficult to source clothes that do not make them look frumpy or do not fit. We have an idea we would like an apple with the peel unravelling and possibly the silhouette of a woman's body coming out of the peel. The lark reed represents the womans body shape and dressing it.

Target Market(s)

modern mature aged woman

Industry/Entity Type

Clothing

Contact Information for Business Card

abn: 41270386915
will provide email at a later date
a spiel re clothes for modern woman???

Font styles to use
Serif
Sans Serif

Requirements
Must have
• will need name - ABN -will need email address but still working on that (TBA)
Nice to have
• picture of an apple with its peel coming off and possibly the silhouette of a woman coming out. the issue a lot of women in the over 50 range have is that the clothing is very dated or makes the woman frumpy. we are providing clothes for the woman who has difficulty in finding fashionable clothes in their size.
Should not have
• don't want childlike

```html
<!DOCTYPE html>
<html lang="en">
<head>
<meta charset="utf-8">
<title>Lark Reed — Business Card</title>
<link rel="stylesheet" href="https://fonts.googleapis.com/css2?family=Arimo:wght@400&family=Cinzel:wght@500&display=swap">
<style>
  :root {
    --backdrop: #ececec;
    --card-white: #ffffff;
    --leaf-green: #badd7e;
    --leaf-green-soft: #c6e394;
    --olive-ink: #7c8a69;
    --pale-text: #f4fbe9;
  }
  * { margin: 0; padding: 0; box-sizing: border-box; }
  html, body {
    width: 1200px; height: 999px; overflow: hidden;
    background: var(--backdrop);
    font-family: "Arimo", Arial, sans-serif;
  }
  .canvas { position: relative; width: 1200px; height: 999px; }

  /* Front: brand side */
  .card-front {
    position: absolute; left: 65px; top: 170px;
    width: 398px; height: 658px;
    background: var(--card-white);
  }
  .brand-mark {
    position: absolute; left: 50%; top: 215px;
    width: 72px; height: 72px; margin-left: -36px;
  }
  .brand-name {
    position: absolute; left: 0; right: 0; top: 422px;
    text-align: center;
    font-family: "Cinzel", Georgia, serif;
    font-weight: 500; font-size: 38px; letter-spacing: 1px;
    color: var(--olive-ink);
  }
  .brand-tagline {
    position: absolute; left: 0; right: 0; top: 459px;
    text-align: center;
    font-size: 15.5px; color: var(--olive-ink);
  }

  /* Back: contact side */
  .card-back {
    position: absolute; left: 512px; top: 311px;
    width: 625px; height: 376px;
    background: var(--leaf-green);
  }
  .name-bar {
    position: absolute; left: 0; width: 276px; height: 32px;
    background: var(--card-white);
    padding-right: 45px;
    text-align: right;
    font-size: 22px; line-height: 32px;
    color: var(--leaf-green);
  }
  .name-bar--first { top: 151px; }
  .name-bar--second { top: 193px; }
  .contact-line {
    position: absolute; left: 312px;
    font-size: 15px; color: var(--pale-text);
  }
  .contact-line--phone-a { top: 160px; }
  .contact-line--phone-b { top: 204px; }
  .contact-line--email { top: 243px; }
  .abn {
    position: absolute; right: 14px; bottom: 11px;
    font-size: 12.5px; color: var(--pale-text);
  }
</style>
</head>
<body>
<main class="canvas">
  <section class="card-front">
    <svg class="brand-mark" viewBox="0 0 72 72" aria-hidden="true">
      <circle cx="36" cy="36" r="36" fill="var(--leaf-green-soft)"/>
    </svg>
    <h1 class="brand-name">LARK REED</h1>
    <p class="brand-tagline">weekend collection for petite women</p>
  </section>

  <section class="card-back">
    <p class="name-bar name-bar--first">Mara Quinlan</p>
    <p class="name-bar name-bar--second">Helen Darby</p>
    <p class="contact-line contact-line--phone-a">0411 582 307</p>
    <p class="contact-line contact-line--phone-b">0433 719 264</p>
    <p class="contact-line contact-line--email">larkreedpetite@mailbox.net</p>
    <p class="abn">abn: 41270386915</p>
  </section>
</main>
</body>
</html>
```